Business Card for Yachting Management Company

Need a business card design for a new yachting project management company. Attached is the logo for the company.
Our clients are large yacht owners and captains.
Design must be in the style of the logo. Modern, elegant.

Example of data to show:
Oliver Tennant
Project Manager
(+34) 612 870 334
oliver@quarvel.net
Quarvel Management - Marisol Tower, Office 22 - NDR - Palma de Mallorca

The data above will have to be changed (by me) for the different people in the company over the next years.

Will be printed using CardHarbor (Lustrel Business Cards). They provide these guidelines for the size:
"the actual size of the card is 1050 x 600 pixels. However, the full bleed size is 1083 x 633 pixels, and the safe printing area is 1008 x 558 pixels."

```html
<!DOCTYPE html>
<html lang="en">
<head>
<meta charset="utf-8">
<title>Quarvel Management – Business Card</title>
<link href="https://fonts.googleapis.com/css2?family=Arimo:wght@400;700&family=Michroma&display=swap" rel="stylesheet">
<style>
  :root {
    --backdrop: #2b2b2b;
    --card-white: #ffffff;
    --brand-blue: #0a72c2;
    --brand-blue-soft: #2a8ad8;
    --text-light: #ffffff;
  }
  * { box-sizing: border-box; margin: 0; padding: 0; }
  html, body {
    width: 1200px; height: 1015px; overflow: hidden;
    background: var(--backdrop);
  }
  .sheet {
    position: relative; width: 1200px; height: 1015px;
    display: flex; flex-direction: column; align-items: center; justify-content: center; gap: 40px;
  }
  .card {
    position: relative; width: 800px; height: 457px;
    box-shadow: 0 10px 30px rgba(0,0,0,.55);
    overflow: hidden;
    font-family: "Arimo", Arial, sans-serif;
  }
  .card--front { background: var(--card-white); }
  .card--back { background: var(--brand-blue); color: var(--text-light); }

  .brand-name {
    position: absolute; display: flex; align-items: center; gap: 14px;
    font-family: "Arimo", Arial, sans-serif; font-weight: 700; line-height: 1;
    white-space: nowrap;
  }
  .brand-name__mark { display: block; flex: none; }

  .card--front .brand-name {
    left: 50%; top: 50%; transform: translate(-50%, -50%);
    font-size: 44px; color: var(--brand-blue);
  }
  .card--front .brand-name__mark { width: 34px; height: 34px; background: var(--brand-blue); }

  .card--back .brand-name {
    right: 56px; top: 110px;
    font-size: 34px; color: var(--brand-blue-soft);
  }
  .card--back .brand-name__mark { width: 26px; height: 26px; background: var(--brand-blue-soft); }

  .details { position: absolute; left: 70px; top: 190px; }
  .details__name { font-family: "Michroma", sans-serif; font-weight: 400; font-size: 22px; letter-spacing: 1px; text-transform: uppercase; }
  .details__role { font-size: 17px; margin-top: 2px; }
  .contact { list-style: none; margin-top: 38px; font-size: 17px; }
  .contact li { display: flex; align-items: center; gap: 8px; line-height: 1.35; }
  .contact svg { width: 16px; height: 16px; fill: none; stroke: var(--text-light); stroke-width: 1.8; }
  .address { font-style: normal; margin-top: 36px; font-size: 17px; line-height: 1.3; }
  .address__company { font-weight: 700; }
</style>
</head>
<body>
<main class="sheet">
  <section class="card card--front" aria-label="Card front">
    <div class="brand-name">
      <span class="brand-name__mark" aria-hidden="true"></span>
      <span>Quarvel Management</span>
    </div>
  </section>

  <section class="card card--back" aria-label="Card back">
    <div class="brand-name" aria-hidden="true">
      <span class="brand-name__mark"></span>
      <span>Quarvel Management</span>
    </div>
    <div class="details">
      <h1 class="details__name">Oliver Tennant</h1>
      <p class="details__role">Project Manager</p>
      <ul class="contact">
        <li>
          <svg viewBox="0 0 24 24" aria-hidden="true"><path d="M5 3h4l2 5-2.5 1.5a11 11 0 0 0 6 6L16 13l5 2v4a2 2 0 0 1-2 2A16 16 0 0 1 3 5a2 2 0 0 1 2-2z"/></svg>
          (+34) 612 870 334
        </li>
        <li>
          <svg viewBox="0 0 24 24" aria-hidden="true"><rect x="3" y="5" width="18" height="14" rx="1"/><path d="M3 6l9 7 9-7"/></svg>
          oliver@quarvel.net
        </li>
      </ul>
      <address class="address">
        <span class="address__company">Quarvel Management</span><br>
        Marisol Tower, Office 22 - NDR<br>
        Palma de Mallorca
      </address>
    </div>
  </section>
</main>
</body>
</html>
```